Digital ad to Parent Funnel

Those Puddle Jumpers works with preschoolers (also ages 2-8) doing hands-on activities that are Science Tech Engineering and Math (STEM) as a service business. The design is subtly colorful with the attached swatch definitions. Hexagons are a theme on the website.
www.thosepuddlejumpers.com
The purpose is on social media with a call to action to a landing page. I'd like placeholder text so I can be the copywriter. The banner I see is vertical, longer than wider. Design elements are welcoming, cheerful, and concrete. Pictures included are thematic for reference
https://www.pinterest.com/puddlejumpersKV/website-mood-board/
I'd like fonts that are more used than Dosis, which has a child-like font but doesn't render well online. Versatile design desired for deferring ad sizes, if possible. My laptop has InDesign.
Thanks!

```html
<!DOCTYPE html>
<html lang="en">
<head>
<meta charset="utf-8">
<title>Those Puddle Jumpers – Parent Ad Banner</title>
<link rel="stylesheet" href="https://fonts.googleapis.com/css2?family=Dosis:wght@700;800&family=Open+Sans:wght@400;600;700&display=swap">
<style>
  :root {
    --page-bg: #e9eaec;
    --purple: #5e2d8f;
    --purple-deep: #4a1f75;
    --yellow: #f4e631;
    --headline-yellow: #f7ea2e;
    --sky: #29a8e0;
    --sky-deep: #1b8fd0;
    --orange: #f7a73a;
    --green: #3cb54a;
    --green-deep: #2a9a3a;
    --white: #ffffff;
  }
  * { box-sizing: border-box; margin: 0; padding: 0; }
  html, body {
    width: 1200px; height: 1200px; overflow: hidden;
    background: var(--page-bg);
  }
  .ad-banner {
    position: absolute; left: 48px; top: 312px;
    width: 1104px; height: 576px;
    background: var(--purple);
    overflow: hidden;
  }
  .banner-art { position: absolute; inset: 0; width: 1104px; height: 576px; }
  .brand {
    position: absolute; left: 0; top: 72px; width: 500px;
    display: flex; align-items: center; justify-content: center; gap: 12px;
    font-family: 'Dosis', sans-serif; font-weight: 800;
    font-size: 36px; color: var(--white);
  }
  .brand-dot {
    width: 26px; height: 26px; border-radius: 50%;
    background: var(--sky);
  }
  .headline {
    position: absolute; left: 36px; top: 190px;
    font-family: 'Dosis', sans-serif; font-weight: 800;
    font-size: 51px; line-height: 49px;
    color: var(--headline-yellow);
  }
  .body-copy {
    position: absolute; left: 36px; top: 300px; width: 448px;
    font-family: 'Open Sans', sans-serif; font-size: 18px; line-height: 25px;
    color: var(--white);
  }
  .cta-button {
    position: absolute; left: 102px; top: 474px;
    width: 312px; height: 68px; border-radius: 34px;
    background: var(--green);
    box-shadow: inset 0 -4px 0 var(--green-deep);
    display: flex; align-items: center; justify-content: center;
    font-family: 'Dosis', sans-serif; font-weight: 800;
    font-size: 40px; letter-spacing: 1px; color: var(--white);
  }
  .price-bar {
    position: absolute; left: 660px; top: 0; width: 444px; height: 66px;
    display: flex; align-items: center; justify-content: center;
    font-family: 'Open Sans', sans-serif; font-size: 24px; color: var(--white);
  }
  .price-bar strong { font-weight: 700; font-size: 27px; margin: 0 6px; }
  .link-bar {
    position: absolute; left: 624px; top: 510px; width: 480px; height: 66px;
    display: flex; align-items: center; justify-content: center;
    font-family: 'Open Sans', sans-serif; font-size: 18px; color: var(--white);
    white-space: nowrap;
  }
</style>
</head>
<body>
  <div class="ad-banner">
    <svg class="banner-art" viewBox="0 0 1104 576" xmlns="http://www.w3.org/2000/svg">
      <defs>
        <linearGradient id="photo-tones" x1="0" y1="0" x2="1" y2="1">
          <stop offset="0" stop-color="#e9dbe6"/>
          <stop offset="0.55" stop-color="#c9a7bf"/>
          <stop offset="1" stop-color="#5a4a6a"/>
        </linearGradient>
      </defs>
      <polygon class="edge-shadow" points="560,0 640,66 590,228 650,324 596,420 614,510 580,576 520,576 520,0" fill="var(--purple-deep)"/>
      <rect class="top-bar" x="624" y="0" width="480" height="66" fill="var(--orange)"/>
      <rect class="bottom-bar" x="606" y="510" width="498" height="66" fill="var(--sky)"/>
      <polygon role="img" aria-label="Photo of a smiling young boy holding up a spinning rainbow pinwheel by a bright window"
        points="648,66 1104,66 1104,510 624,510 606,420 660,324 600,228 648,84" fill="url(#photo-tones)"/>
      <polygon class="shard-yellow" points="502,0 610,70 538,216" fill="var(--yellow)"/>
      <polygon class="shard-blue" points="586,0 684,0 624,48" fill="var(--sky)"/>
      <polygon class="shard-blue" points="654,72 588,168 666,252" fill="var(--sky-deep)"/>
      <polygon class="shard-yellow" points="496,234 616,218 548,380" fill="var(--yellow)"/>
      <polygon class="shard-blue" points="508,344 600,344 604,450" fill="var(--sky)"/>
      <polygon class="shard-yellow" points="498,412 600,486 560,576" fill="var(--yellow)"/>
      <polygon class="shard-yellow" points="548,576 604,520 604,576" fill="var(--yellow)"/>
    </svg>

    <div class="brand"><span class="brand-dot"></span>Those Puddle Jumpers</div>

    <h1 class="headline">Children matter,<br>how about you?</h1>
    <p class="body-copy">As a Maker of Experiences, Those Puddle Jumpers brings you relief. She increases the potential and joy in your children with STEM activities. Playgroups or Mother's Helper.</p>
    <div class="cta-button">MESSAGE</div>

    <div class="price-bar">One hour is <strong>$8</strong> per 2-8 yo</div>
    <div class="link-bar">More...at thosepuddlejumpers.com/at-home-mom</div>
  </div>
</body>
</html>
```